Flyer-Design für Hörgeräteakustik
Ich war top zufrieden! Bereits der erste Flyer war super und nach einer Nachbearbeitung war er perfekt :)
Zielgruppe
Hörgeräteakustik - Die Zielgruppe sind Menschen ab 50 J.
Aufgabenstellung
BILDMATERIAL FOLGT!
Format: Quadrat - Maße noch unentschlossen
Seitenanzahl: 4 Seiten
Falzart: Einbruchfalz
Texte:
Philosophie
Ich möchte Ihr Leben hörbar verbessern
Meine Arbeit als Hörakustik-Meisterin ist für mich nicht nur ein Beruf, sondern auch meine Berufung.
Dank modernster Technik lassen sich unterschiedliche Höreinschränkungen sehr gut ausgleichen. Um gemeinsam die für Sie optimale Hörlösung finden, nehme ich mir Zeit und berate Sie ausführlich und herstellerunabhängig. Mir ist es wichtig, eine Lösung zu finden, die perfekt zu Ihnen und Ihrem Leben passt.
Damit sich Menschen mit eingeschränkter Mobilität professionell von mir beraten und versorgen lassen können, besuche ich sie gerne in ihrer gewohnten Umgebung. Dank einer kleinen Werkstatt in meinem Transporter und der mobilen Messtechnik kann ich alle Leistungen auch bei Ihnen vor Ort erbringen.
Ich vereinbare auch gerne individuelle Termine außerhalb der Ladenöffnungszeiten, sodass einer professionellen Hörsystemversorgung nichts im Wege steht.
Leistungen
-Kostenloser Hörtest
-Hörberatung
-Unverbindliches Probetragen
-Hausbesuch-Service
-Hörgeräte-Fernanpassung
-Angepasster Gehörschutz
Der Weg zum guten Hören
1. Hörtest und Höranalyse
Als ersten Schritt führe ich mit Ihnen einen Hörtest und eine Höranalyse durch. Dabei nehme ich mir Zeit und überprüfe ausführlich Ihr Hörvermögen.
2. Individuelle Hörberatung
Wenn ich bei den Hörmessungen eine Hörminderung feststelle, setzen wir uns zusammen und finden gemeinsam die für Sie optimale Hörlösung. Auf Grundlage Ihrer Wünsche und Bedürfnisse sowie der Ergebnisse der Hörmessung wählen wir dann gemeinsam Probegeräte aus.
3. Individuelle Anpassung
Die von Ihnen ausgewählten Hörgeräte passe ich individuell Ihrem Hörvermögen an.
4. Unverbindliches Probetragen<..

```html
<!DOCTYPE html>
<html lang="de">
<head>
<meta charset="utf-8">
<title>Flyer Hörakustik – Innenseiten und Titel</title>
<link rel="stylesheet" href="https://fonts.googleapis.com/css2?family=Open+Sans:wght@400;600;700&family=Playfair+Display:wght@600&display=swap">
<style>
  :root{
    --bg:#e6e6e7;
    --paper:#ffffff;
    --rose:#c9939f;
    --rose-light:#d4a7b2;
    --rose-text:#c0788e;
    --sage:#d3e4c3;
    --sage-text:#9cc28a;
    --ink:#555a5c;
    --photo-warm:#d9d6d4;
    --photo-cool:#bfc4c8;
  }
  *{box-sizing:border-box;margin:0;padding:0}
  html,body{width:1200px;height:551px;overflow:hidden;background:var(--bg)}
  body{font-family:"Open Sans",sans-serif;color:var(--ink)}
  .flyer{position:absolute;left:30px;top:85px;display:flex;width:1140px;height:380px;box-shadow:0 6px 18px rgba(0,0,0,.12)}
  .panel{position:relative;width:380px;height:380px;overflow:hidden;background:var(--paper)}

  /* Philosophie */
  .photo{position:absolute;left:0;right:0}
  .philosophy .photo{top:0;height:150px;background:linear-gradient(100deg,#8a8a8a 0 6%,#f1f1f1 6% 45%,var(--photo-cool) 75%,#9c9c9c)}
  .philosophy .text{position:absolute;top:162px;left:22px;right:22px}
  .philosophy h2{font-family:"Playfair Display",serif;font-weight:600;font-size:23px;color:var(--rose-text);line-height:1}
  .philosophy .lead{font-size:12.5px;color:var(--sage-text);margin:3px 0 9px}
  .philosophy p{font-size:6.9px;line-height:1.5;margin-bottom:4px;text-align:justify}
  .philosophy p.intro{font-weight:700}

  /* Kontakt */
  .contact{background:var(--rose-light);color:#fff}
  .contact .text{position:absolute;top:26px;left:24px;right:24px}
  .contact h2{font-family:"Playfair Display",serif;font-weight:600;font-size:17px;letter-spacing:.5px;margin-bottom:10px}
  .contact p{font-size:6.9px;line-height:1.5;margin-bottom:7px}
  .contact .strong{font-weight:700}
  .contact-band{position:absolute;left:0;right:0;bottom:0;height:72px;background:var(--sage);display:flex;justify-content:space-between;padding:16px 20px 0;color:#fff}
  .contact-band ul{list-style:none;font-size:7px;line-height:1.9}
  .contact-band li{display:flex;align-items:center;gap:5px}
  .contact-band svg{width:9px;height:9px;flex:none}
  .dot{width:8px;height:8px;border-radius:50%;background:#fff;flex:none}

  /* Titel */
  .cover .brand{position:absolute;top:38px;right:26px;display:flex;align-items:center;gap:8px}
  .cover .brand-mark{width:14px;height:14px;border-radius:50%;background:var(--rose-text)}
  .cover .brand-name{font-family:"Open Sans",sans-serif;font-weight:600;font-size:15px;color:var(--rose-text)}
  .cover .photo{top:92px;height:200px;background:linear-gradient(90deg,#c3c7ca,var(--photo-warm) 45%,#e2c9a3 70%,#d8d2cc)}
  .cover .web-band{position:absolute;left:0;right:0;top:278px;height:82px;background:var(--rose);display:flex;align-items:center;justify-content:center}
  .cover .web{font-size:17px;color:#fff;letter-spacing:.5px}
  .cover .sage-strip{position:absolute;left:0;right:0;bottom:0;height:20px;background:var(--sage)}
</style>
</head>
<body>
<div class="flyer">

  <section class="panel philosophy">
    <div class="photo" role="img" aria-label="Foto: Hörakustikerin berät einen älteren Kunden"></div>
    <div class="text">
      <h2>Philosophie</h2>
      <div class="lead">Ich möchte Ihr Leben hörbar verbessern</div>
      <p class="intro">Meine Arbeit als Hörakustik-Meisterin ist für mich nicht nur ein Beruf, sondern auch meine Berufung.</p>
      <p>Dank modernster Technik lassen sich unterschiedliche Höreinschränkungen sehr gut ausgleichen. Um gemeinsam die für Sie optimale Hörlösung finden, nehme ich mir Zeit und berate Sie ausführlich und herstellerunabhängig. Mir ist es wichtig, eine Lösung zu finden, die perfekt zu Ihnen und Ihrem Leben passt.</p>
      <p>Damit sich Menschen mit eingeschränkter Mobilität professionell von mir beraten und versorgen lassen können, besuche ich sie gerne in ihrer gewohnten Umgebung. Dank einer kleinen Werkstatt in meinem Transporter und der mobilen Messtechnik kann ich alle Leistungen auch bei Ihnen vor Ort erbringen.</p>
      <p>Ich vereinbare auch gerne individuelle Termine außerhalb der Ladenöffnungszeiten, sodass einer professionellen Hörsystemversorgung nichts im Wege steht.</p>
    </div>
  </section>

  <section class="panel contact">
    <div class="text">
      <h2>ICH BIN GERNE FÜR SIE DA</h2>
      <p>Sie erreichen mich während der Öffnungszeiten in meinem Hörakustik-Fachgeschäft. Bequem und kostenlos parken können Sie direkt davor.</p>
      <p><span class="strong">Marena Bramstell Hörakustik</span><br>Lindenhofweg 4<br>12345 Musterstadt</p>
      <p>Öffnungszeiten:<br>Mo, Di, Do, Fr 8 – 14 Uhr</p>
      <p>Sehr gerne können wir auch einen persönlichen Termin außerhalb dieser Öffnungszeiten vereinbaren. Dieser kann in meinem Hörakustik-Fachgeschäft oder in Ihrer gewohnten Umgebung stattfinden.</p>
      <p>Zusätzliche Zeiten für individuelle Termine (im Fachgeschäft / Hausbesuche):<br><span class="strong">Mo, Di, Do, Fr ab 14.30 Uhr<br>Mi ganztägig<br>Sa 10 – 16 Uhr</span></p>
      <p>Nehmen Sie am besten noch heute Kontakt zu mir auf.</p>
    </div>
    <div class="contact-band">
      <ul>
        <li><svg viewBox="0 0 10 10"><path fill="#fff" d="M2 1l2 2-1 1.2a6 6 0 0 0 2.8 2.8L7 6l2 2-1.2 1.3C4.5 9 1 5.5.7 2.2z"/></svg>02345 678901</li>
        <li><svg viewBox="0 0 10 10"><rect x="2.5" y=".5" width="5" height="9" rx="1" fill="#fff"/></svg>0170 1234567</li>
      </ul>
      <ul>
        <li><svg viewBox="0 0 10 10"><rect x=".5" y="2" width="9" height="6" fill="#fff"/><path d="M.5 2l4.5 3.5L9.5 2" stroke="#d3e4c3" fill="none"/></svg>info@hoerakustik-bramstell.de</li>
        <li><svg viewBox="0 0 10 10"><circle cx="5" cy="5" r="4.2" fill="none" stroke="#fff"/><path d="M1 5h8M5 .8v8.4" stroke="#fff"/></svg>www.hoerakustik-bramstell.de</li>
      </ul>
      <ul>
        <li><span class="dot"></span>Marena Bramstell Hörakustik</li>
        <li><span class="dot"></span>marena_bramstell_hoerakustik</li>
      </ul>
    </div>
  </section>

  <section class="panel cover">
    <div class="brand">
      <span class="brand-mark"></span>
      <span class="brand-name">Marena Bramstell Hörakustik</span>
    </div>
    <div class="photo" role="img" aria-label="Foto: Hörakustikerin untersucht das Ohr einer Kundin mit einem Otoskop"></div>
    <div class="web-band"><span class="web">www.hoerakustik-bramstell.de</span></div>
    <div class="sage-strip"></div>
  </section>

</div>
</body>
</html>
```